Flyer für junges Unternehmen im Bereich Maschinenbau
Zielgruppe
Wir sind ein junges Unternehmen im Bereich Maschinenbau und sind spezialisiert auf Lasern von Blechen und Rohren und die gesamte Bearbeitung von Metallbaugruppen. Unsere Zielgruppe: Agrartechnik, Metallbauer, Industriekunden, Maschinenbauer - kleine sowie große Unternehmen
Aufgabenstellung
Es soll ein Flyer in DIN A5 werden, der von beiden Seiten bedruckt wird. Es soll herausstechen, was wir machen und worauf wir spezialisiert sind. Auch alle Bearbeitungsabteilung sollen erwähnt werden. Der Kunde soll auf den ersten Blick sehen, dass wir in der Metallbearbeitung dem Kunden ein Gesamtprodukt mit allen Möglichkeiten anbieten können. Der Flyer soll modern sein und Bilder im Vordergrund stehen. Auf unserer Website kann man gut erkennen, was wir alles machen.
Wenn noch andere Bilder benötigt werden, können Sie gerne auch nach Stock-Bilder recherchieren.

```html
<!DOCTYPE html>
<html lang="de">
<head>
<meta charset="utf-8">
<title>Kerbwerk Laser GmbH – Flyer</title>
<link rel="stylesheet" href="https://fonts.googleapis.com/css2?family=Orbitron:wght@800&family=Montserrat:wght@400;700&family=Lexend:wght@400;600&display=swap">
<style>
:root{
  --stage:#8e8e8e;
  --ink:#0a0a0c;
  --blue:#0f8bd2;
  --blue-dark:#0a6fae;
  --white:#ffffff;
  --tile:#1f1f23;
  --metal-light:#f4f4f5;
  --metal-mid:#c9cacd;
  --text-dark:#17171a;
  --logo-grey:#b9bcc2;
}
*{margin:0;padding:0;box-sizing:border-box}
html,body{width:1200px;height:1117px;overflow:hidden;background:var(--stage)}
.page{position:absolute;top:194px;width:513px;height:729px;overflow:hidden;background:var(--ink);font-family:"Montserrat",sans-serif}
.page--front{left:75px}
.page--back{left:613px}
.metal{position:absolute;left:0;right:0;background:linear-gradient(180deg,var(--metal-mid) 0%,var(--metal-light) 35%,#e2e3e6 70%,var(--metal-mid) 100%)}
.brand{position:absolute;display:flex;align-items:center;gap:10px;font-family:"Montserrat",sans-serif;font-weight:700;color:var(--logo-grey);line-height:1.1}
.brand__dot{border:4px solid var(--blue);border-radius:50%;flex:none}
.blue-bar{position:absolute;left:0;right:0;bottom:0;height:14px;background:var(--blue)}

/* front */
.front-photo{position:absolute;left:0;top:0;width:513px;height:500px;background:radial-gradient(ellipse at 55% 72%,#e9ecff 0%,#7a6fd6 14%,#2d2a6a 38%,#0c0c1e 70%,#050508 100%)}
.front .metal{top:495px;bottom:0}
.front .brand{right:24px;top:58px;font-size:26px}
.front .brand__dot{width:44px;height:44px}
.headline{position:absolute;left:0;right:0;top:326px;text-align:center;font-family:"Orbitron",sans-serif;font-weight:800;font-size:27px;line-height:30px;letter-spacing:.3px}
.headline__line1{color:var(--white);display:block}
.headline__line2{color:var(--blue);display:block;font-size:28px}
.hexes{position:absolute;left:0;top:398px;width:513px;height:200px}
.front-intro{position:absolute;left:30px;right:30px;top:607px;text-align:center;font-size:12.4px;line-height:15px;color:var(--text-dark)}
.front-intro b{font-weight:700}
.url-band{position:absolute;left:115px;top:672px;width:284px;height:44px;background:linear-gradient(180deg,var(--blue) 0%,var(--blue-dark) 100%);clip-path:polygon(6% 0,94% 0,100% 100%,0 100%);display:flex;align-items:center;justify-content:center;font-family:"Lexend",sans-serif;font-size:19px;color:var(--white)}

/* back */
.back-photo{position:absolute;left:0;top:0;width:513px;height:400px;background:radial-gradient(ellipse at 55% 35%,#6b6257 0%,#3a312a 30%,#1a1512 60%,#070606 100%)}
.back .metal{top:392px;height:216px}
.back .brand{left:346px;top:46px;font-size:16px}
.back .brand__dot{width:28px;height:28px;border-width:3px}
.services{position:absolute;left:45px;top:217px;width:423px;height:274px;background:var(--ink);border:4px solid var(--white);box-shadow:0 0 0 3px var(--ink)}
.services__title{position:absolute;left:139px;top:202px;width:232px;height:34px;background:var(--blue);clip-path:polygon(7% 0,93% 0,100% 50%,93% 100%,7% 100%,0 50%);display:flex;align-items:center;justify-content:center;font-family:"Lexend",sans-serif;font-weight:600;font-size:20px;color:var(--white);box-shadow:0 0 0 4px var(--ink)}
.tile{position:absolute;background:var(--tile);border-radius:8px;display:flex;flex-direction:column;align-items:center;color:var(--white);font-family:"Lexend",sans-serif;font-weight:600;font-size:12px;line-height:14px;text-align:center}
.tile__icon{width:54px;height:54px;margin-top:10px;margin-bottom:10px;border-radius:6px;background:#e6e7ea}
.tile--row1{top:247px;width:88px;height:110px}
.tile--row2{top:371px;width:92px;height:100px}
.back-intro{position:absolute;left:40px;right:40px;top:506px;text-align:center;font-size:9.8px;line-height:11.6px;color:var(--text-dark)}
.back-intro p+p{margin-top:6px}
.contact{position:absolute;font-family:"Lexend",sans-serif;color:var(--white)}
.contact__row{display:flex;align-items:center;gap:8px;height:22px;font-size:14px;white-space:nowrap}
.contact__row--strong{font-weight:600;font-size:15px}
.contact__icon{width:15px;height:15px;flex:none}
.contact--left{left:60px;top:624px;width:232px}
.contact--right{left:306px;top:624px;width:190px}
.address{display:flex;gap:8px;font-size:15px;line-height:19px}
.hours{margin-top:6px;color:var(--blue);font-weight:600;font-size:11.5px;line-height:15px;white-space:nowrap}
</style>
</head>
<body>

<section class="page page--front front">
  <div class="front-photo" role="img" aria-label="Foto: Schweißer mit Schutzhelm bei der Arbeit, Funkenflug in blauem Licht"></div>
  <div class="metal"></div>

  <div class="brand"><span class="brand__dot"></span><span>Kerbwerk<br>Laser GmbH</span></div>

  <h1 class="headline">
    <span class="headline__line1">INNOVATIVE ROHR- UND</span>
    <span class="headline__line2">BLECHBEARBEITUNG</span>
  </h1>

  <svg class="hexes" viewBox="0 0 513 200">
    <defs>
      <linearGradient id="silver" x1="0" y1="0" x2="0" y2="1">
        <stop offset="0" stop-color="#f2f2f4"/><stop offset=".5" stop-color="#9a9ca2"/><stop offset="1" stop-color="#e8e8ea"/>
      </linearGradient>
      <linearGradient id="photoLaser" x1="0" y1="0" x2="1" y2="1">
        <stop offset="0" stop-color="#cfd2d6"/><stop offset=".6" stop-color="#6a6c70"/><stop offset="1" stop-color="#b07a3a"/>
      </linearGradient>
      <linearGradient id="photoSheet" x1="0" y1="0" x2="1" y2="1">
        <stop offset="0" stop-color="#9a9ea4"/><stop offset=".5" stop-color="#dfe1e4"/><stop offset="1" stop-color="#7d8187"/>
      </linearGradient>
      <linearGradient id="photoGear" x1="0" y1="0" x2="1" y2="1">
        <stop offset="0" stop-color="#5a6a9a"/><stop offset=".5" stop-color="#b9bccc"/><stop offset="1" stop-color="#3a3550"/>
      </linearGradient>
    </defs>
    <polygon points="102,2 187,51 187,149 102,198 17,149 17,51" fill="url(#silver)"/>
    <polygon points="102,12 178,56 178,144 102,188 26,144 26,56" fill="#0a0a0c"/>
    <g role="img" aria-label="Foto: Laserschneidkopf schneidet ein Metallrohr"><polygon points="102,19 172,59.5 172,140.5 102,181 32,140.5 32,59.5" fill="url(#photoLaser)"/></g>

    <polygon points="257,2 342,51 342,149 257,198 172,149 172,51" fill="url(#silver)"/>
    <polygon points="257,12 333,56 333,144 257,188 181,144 181,56" fill="#0a0a0c"/>
    <g role="img" aria-label="Foto: lasergeschnittene Blechteile"><polygon points="257,19 327,59.5 327,140.5 257,181 187,140.5 187,59.5" fill="url(#photoSheet)"/></g>

    <polygon points="411,2 496,51 496,149 411,198 326,149 326,51" fill="url(#silver)"/>
    <polygon points="411,12 487,56 487,144 411,188 335,144 335,56" fill="#0a0a0c"/>
    <g role="img" aria-label="Foto: Zahnräder beim Fräsen"><polygon points="411,19 481,59.5 481,140.5 411,181 341,140.5 341,59.5" fill="url(#photoGear)"/></g>
  </svg>

  <p class="front-intro">Kerbwerk Laser GmbH ist ein starker Partner im Bereich <b>Laserschneiden</b> von Blechen und Rohren sowie der weiteren <b>Bearbeitung ganzer Baugruppen</b> mit dem Ziel kundenorientiert zu agieren.</p>

  <div class="url-band">www.kerbwerk-laserteile.de</div>
  <div class="blue-bar"></div>
</section>

<section class="page page--back back">
  <div class="back-photo" role="img" aria-label="Foto: Schweißer in Arbeitskleidung in dunkler Werkhalle mit Funken und Rauch"></div>
  <div class="metal"></div>

  <div class="brand"><span class="brand__dot"></span><span>Kerbwerk<br>Laser GmbH</span></div>

  <div class="services"></div>
  <h2 class="services__title">Unsere Leistungen</h2>

  <div class="tile tile--row1" style="left:63px"><div class="tile__icon" role="img" aria-label="Symbol Rohrbearbeitung"></div>Rohre</div>
  <div class="tile tile--row1" style="left:163px"><div class="tile__icon" role="img" aria-label="Symbol Blechteile"></div>Bleche</div>
  <div class="tile tile--row1" style="left:262px"><div class="tile__icon" role="img" aria-label="Symbol Drehen und Fräsen"></div>Drehen und Fräsen</div>
  <div class="tile tile--row1" style="left:361px"><div class="tile__icon" role="img" aria-label="Symbol Abkanten"></div>Abkanten</div>
  <div class="tile tile--row2" style="left:109px"><div class="tile__icon" role="img" aria-label="Symbol Schweißen"></div>Schweißen</div>
  <div class="tile tile--row2" style="left:210px"><div class="tile__icon" role="img" aria-label="Symbol Konstruktion"></div>Konstruktion</div>
  <div class="tile tile--row2" style="left:311px"><div class="tile__icon" role="img" aria-label="Symbol Oberflächen"></div>Oberflächen</div>

  <div class="back-intro">
    <p>Wir sind ein mittelständisches Unternehmen im Kreis Musterland mit einem modernen Maschinenpark. Von Einzelteilen bis hin zu umfassenden Baugruppen beziehen Sie unsere Produkte in kompromissloser Qualität.</p>
    <p>Durch unsere Fülle an Fertigungsprozessen und unseren Fachkenntnissen begleiten wir Ihr Produkt an einem Standort voll umfänglich von der Idee zum fertigen Produkt. Durch unseren hauseinigen Fuhrpark stellen wir eine pünktliche und mühelose Zustellung sicher.</p>
  </div>

  <div class="contact contact--left">
    <div class="contact__row contact__row--strong">
      <svg class="contact__icon" viewBox="0 0 16 16"><circle cx="8" cy="8" r="8" fill="#0f8bd2"/><path d="M5.2 4.2l1.4-.3.9 2-.9.7c.5 1 1.3 1.8 2.3 2.3l.7-.9 2 .9-.3 1.4c-3.4.2-6.3-2.7-6.1-6.1z" fill="#fff"/></svg>
      +49 (0000) 481200
    </div>
    <div class="contact__row">
      <svg class="contact__icon" viewBox="0 0 16 16"><circle cx="8" cy="8" r="8" fill="#0f8bd2"/><rect x="4" y="5" width="8" height="6" rx="1" fill="none" stroke="#fff" stroke-width="1.1"/><path d="M4.3 5.5L8 8.5l3.7-3" fill="none" stroke="#fff" stroke-width="1.1"/></svg>
      info@kerbwerk-laserteile.de
    </div>
    <div class="contact__row">
      <svg class="contact__icon" viewBox="0 0 16 16"><circle cx="8" cy="8" r="8" fill="#0f8bd2"/><circle cx="8" cy="8" r="4" fill="none" stroke="#fff" stroke-width="1"/><path d="M4 8h8M8 4v8M5.3 5.5h5.4M5.3 10.5h5.4" stroke="#fff" stroke-width=".8"/></svg>
      www.kerbwerk-laserteile.de
    </div>
  </div>

  <div class="contact contact--right">
    <div class="address">
      <svg class="contact__icon" viewBox="0 0 16 16" style="margin-top:2px"><path d="M8 0.5a5.5 5.5 0 0 0-5.5 5.5c0 4 5.5 9.5 5.5 9.5s5.5-5.5 5.5-9.5A5.5 5.5 0 0 0 8 .5z" fill="#0f8bd2"/><circle cx="8" cy="6" r="2" fill="#0a0a0c"/></svg>
      <span>Werkstraße 12<br>12345 Musterstadt</span>
    </div>
    <div class="hours">Mo. - Do. : 7:00 – 16:00 Uhr<br>Fr. : 7:00 – 12:00 Uhr</div>
  </div>

  <div class="blue-bar"></div>
</section>

</body>
</html>
```